Business Card design for construction company

I would like a business card design for a construction company - Harlow Constructions. I have attached the ai logo file for use. I would like the card to be very smart and clean and incorporate only white and the two colours in the logo. I would like the card to have two sides. One side can just have the logo, the other with the relevant information.

Target Market(s)

Building and Construction Clients

Industry/Entity Type

Business

Contact Information for Business Card

Name: Tom Pardoe
Company: Harlow Constructions Pty Limited
Address: 14 Mallee Crescent Carrow Vale 2093
Phone: 0427 531 068
Email: tomp@harlowbuild-example.com.au

Font styles to use
Serif
Sans Serif

Requirements
Must have
• Details noted above
• Logo as provided
• Colours as in logo
• Square edges
• A font that compliments the logo
Should not have
• Any colour other than white and those in logo
• Rounded edges

```html
<!DOCTYPE html>
<html lang="en">
<head>
<meta charset="utf-8">
<title>Harlow Constructions – Business Card Front</title>
<link href="https://fonts.googleapis.com/css2?family=Michroma&display=swap" rel="stylesheet">
<style>
  :root {
    --page-white: #ffffff;
    --brand-blue: #00aeef;
    --brand-grey: #58595b;
    --text-white: #ffffff;
  }
  * { margin: 0; padding: 0; box-sizing: border-box; }
  html, body {
    width: 1200px;
    height: 711px;
    overflow: hidden;
    background: var(--page-white);
  }
  .canvas {
    position: relative;
    width: 1200px;
    height: 711px;
    background: var(--page-white);
  }
  .card-front {
    position: absolute;
    left: 28px;
    top: 26px;
    width: 1147px;
    height: 660px;
    border-radius: 30px;
    background: var(--brand-blue);
    overflow: hidden;
  }
  .name-band {
    position: absolute;
    left: 231px;
    top: 278px;
    right: 0;
    height: 102px;
    background: var(--brand-grey);
    display: flex;
    align-items: center;
    padding-left: 113px;
  }
  .company-name {
    font-family: "Michroma", "Arial", sans-serif;
    font-weight: 400;
    font-size: 20px;
    letter-spacing: 0.06em;
    color: var(--text-white);
    text-transform: uppercase;
    white-space: nowrap;
  }
</style>
</head>
<body>
  <main class="canvas">
    <section class="card-front" aria-label="Business card front">
      <div class="name-band">
        <p class="company-name">Harlow Constructions</p>
      </div>
    </section>
  </main>
</body>
</html>
```